KTR Engineering Business Card Design

We’re looking for an elegant, clean, and timeless business card design that communicates experience, capability, and reliability.

KTR Engineering was established in 1995 , we are a Government Contracting company providing Professional Services to the Ministry of Harbor Works, Frontier Stewardship and the Waypoint Consortium. Our capabilities include: Acquisition & Program Management; Intelligence & Security Operations; Cyber, IT & Network Operations; Lifecycle Logistics & Asset Readiness; C5ISR Systems Engineering & Sustainment.

We want the card to reflect a straightforward, confident approach to business. The design should feel polished and professional without being flashy or overly corporate.

Design Direction
Clean, sophisticated, and uncluttered
Elegant but understated
Strong typography and thoughtful spacing
A timeless aesthetic rather than something overly trendy
Confident and established, with a sense of substance
Easy to read and practical in a real-world business setting

The overall impression should be: “These are experienced professionals who know what they’re doing, do what they say, and can be relied upon.”

We’re open to creative interpretations. The finished card should feel distinctive through its typography, proportions, layout, and attention to detail rather than through excessive graphics or visual effects.

We’re looking for a design that would make a potential client immediately feel that they’re dealing with a capable, trustworthy, and established company.

Company Colors: Navy and Gold/Yellow (but you do not need to use these colors on the card)
Company Name: KTR Engineering Associates, Inc. (known as KTR Engineering)
Website: ktrengineering.example
Company Logo: Navy & Gold (other variations attached)

```html
<!DOCTYPE html>
<html lang="en">
<head>
<meta charset="utf-8">
<title>KTR Engineering – Business Card</title>
<link rel="stylesheet" href="https://fonts.googleapis.com/css2?family=Poppins:wght@400;500;700;800&display=swap">
<style>
  :root {
    --navy: #222c63;
    --gold: #fbe04a;
    --white: #ffffff;
    --stage: #2b2e34;
    --card-w: 540px;
    --card-h: 309px;
  }
  * { box-sizing: border-box; margin: 0; padding: 0; }
  html, body { width: 1200px; height: 985px; overflow: hidden; }
  body {
    background: var(--stage);
    font-family: "Poppins", sans-serif;
    display: flex;
    align-items: center;
    justify-content: center;
    gap: 40px;
  }
  .card {
    position: relative;
    width: var(--card-w);
    height: var(--card-h);
    border-radius: 18px;
    overflow: hidden;
    box-shadow: 0 14px 30px rgba(0,0,0,.35);
  }
  .card-front { background: var(--white); }
  .card-back {
    background: var(--navy);
    display: flex;
    flex-direction: column;
    align-items: center;
    justify-content: center;
    gap: 14px;
  }
  .front-shape { position: absolute; inset: 0; }
  .brand-name {
    position: absolute;
    left: 30px;
    top: 100px;
    font-weight: 800;
    font-size: 26px;
    letter-spacing: -0.5px;
    color: var(--navy);
    line-height: 1;
    white-space: nowrap;
  }
  .brand-name.on-dark { position: static; color: var(--white); font-size: 44px; }
  .back-url {
    color: var(--white);
    font-size: 13px;
    letter-spacing: 3px;
    font-weight: 400;
  }
  .divider {
    position: absolute;
    left: 30px;
    top: 196px;
    width: 340px;
    height: 1.5px;
    background: var(--gold);
  }
  .contact-list {
    position: absolute;
    left: 30px;
    top: 208px;
    list-style: none;
    font-size: 11px;
    color: var(--navy);
    line-height: 1.7;
  }
  .contact-list li { display: flex; align-items: center; gap: 7px; }
  .contact-icon { width: 12px; height: 12px; flex: none; }
  .address {
    position: absolute;
    right: 130px;
    top: 250px;
    text-align: right;
    font-size: 12px;
    font-style: normal;
    color: var(--navy);
    line-height: 1.5;
    font-weight: 500;
    white-space: nowrap;
  }
  .holder {
    position: absolute;
    right: 22px;
    top: 128px;
    text-align: right;
    white-space: nowrap;
  }
  .holder-name {
    font-weight: 700;
    font-size: 14px;
    color: var(--white);
    letter-spacing: 0.4px;
  }
  .holder-title {
    font-size: 12px;
    color: var(--gold);
    font-weight: 400;
  }
</style>
</head>
<body>
  <section class="card card-front">
    <svg class="front-shape" viewBox="0 0 540 309" width="540" height="309" aria-hidden="true">
      <path d="M40 0 A420 330 0 0 1 460 330 L540 330 L540 0 Z" fill="var(--navy)"/>
      <path d="M40 -8 A398 338 0 0 1 438 330" fill="none" stroke="var(--gold)" stroke-width="9"/>
    </svg>
    <div class="brand-name">KTR Engineering</div>
    <div class="divider"></div>
    <ul class="contact-list">
      <li>
        <svg class="contact-icon" viewBox="0 0 12 12"><circle cx="6" cy="6" r="6" fill="var(--gold)"/><path d="M3.6 3.2l1.2-.4.8 1.6-.7.6c.4.8 1 1.4 1.8 1.8l.6-.7 1.6.8-.4 1.2C6.2 8.2 3.8 5.8 3.6 3.2z" fill="var(--navy)"/></svg>
        555-014-2278
      </li>
      <li>
        <svg class="contact-icon" viewBox="0 0 12 12"><circle cx="6" cy="6" r="6" fill="var(--gold)"/><circle cx="6" cy="6" r="3.2" fill="none" stroke="var(--navy)" stroke-width=".9"/><path d="M2.8 6h6.4M6 2.8v6.4" stroke="var(--navy)" stroke-width=".8"/></svg>
        www.ktrengineering.example
      </li>
    </ul>
    <address class="address">
      1480 Harborline Avenue<br>
      Suite 310, Eastport, ZZ 40117
    </address>
    <div class="holder">
      <div class="holder-name">MARCUS REED</div>
      <div class="holder-title">Manager</div>
    </div>
  </section>

  <section class="card card-back">
    <div class="brand-name on-dark">KTR Engineering</div>
    <div class="back-url">www.ktrengineering.example</div>
  </section>
</body>
</html>
```